依頼概要
■ 依頼の目的/概要
定期的にお客様に郵送する情報誌のデザインをお願いします。

当社は輸入住宅の設計・施工、リノベーション事業を行っております。輸入住宅や高価格のリノベーション工事をされるお客様向けのセンスの良いダイレクトメールの基本デザインをしていただければと思います。

■依頼詳細
サイズ:A3サイズ両面2つ折り
印刷方法:輪転機(赤、黒2色刷り、黒1色でも構いません)
ファイル形式:EXCEL
デザインの希望:英字新聞のようなデザインが良いかと思っています。
現在のDM:添付ファイル「ミルネ通信10月号」をご覧ください。
掲載内容:会社の近況報告、イベント情報、かんたんな読み物

■要望点
定期的に発行するダイレクトメールの基本デザインですので、内容の記載は必要ありません。当社のイメージにあって、長く使えるセンスの良いデザインが募集できればと思います。

会社の詳細はホームページをご覧ください。
輸入住宅の設計・施工
http://www.tamaroutei.com/
リノベーション
http://www.kovanta-remake.com/
依頼金額を23760円に変更して、延長しました。
英字新聞のようなデザインの提案が無く、提案の期限を延長しました。
現在のデザインにとらわれないデザインの提案を期待しています。

デザインが一番英字新聞らしかった。

良いデザインありがとうございます。

```html
<!DOCTYPE html>
<html lang="ja">
<head>
<meta charset="utf-8">
<title>豊かなくらし No.4</title>
<link rel="stylesheet" href="https://fonts.googleapis.com/css2?family=Noto+Serif+JP:wght@400;700;900&family=Noto+Sans+JP:wght@400;700&display=swap">
<style>
  :root {
    --ink: #1a1a1a;
    --paper: #ffffff;
    --rule: #222222;
    --soft-rule: #9a9a9a;
    --photo-dark: #3a3a3a;
    --photo-light: #9c9c9c;
  }
  * { box-sizing: border-box; margin: 0; padding: 0; }
  html, body { width: 846px; height: 1200px; overflow: hidden; background: var(--paper); }
  body { font-family: "Noto Serif JP", serif; color: var(--ink); position: relative; }

  .masthead { position: absolute; left: 22px; right: 22px; top: 18px; height: 160px; border-bottom: 4px double var(--rule); }
  .masthead__tagline { position: absolute; left: 0; right: 0; top: 4px; text-align: center; font-size: 15px; letter-spacing: 1px; }
  .masthead__title { position: absolute; left: 0; right: 0; top: 36px; text-align: center; font-size: 82px; font-weight: 900; letter-spacing: 10px; line-height: 1; }
  .brand { position: absolute; right: 0; top: 50px; width: 116px; height: 82px; background: var(--ink); color: var(--paper); display: flex; align-items: center; justify-content: center; font-size: 26px; font-weight: 700; }

  .sidebar { position: absolute; left: 22px; top: 190px; width: 152px; bottom: 52px; }
  .issue { border-top: 3px solid var(--rule); border-bottom: 1px solid var(--rule); padding: 14px 0 8px; font-size: 38px; font-weight: 900; }
  .issue-date { font-size: 15px; padding: 12px 0 16px; border-bottom: 3px solid var(--rule); }
  .topic { margin-top: 22px; }
  .topic__head { font-size: 20px; font-weight: 900; border-bottom: 1px solid var(--rule); padding-bottom: 6px; margin-bottom: 12px; }
  .topic__body { font-size: 12.5px; line-height: 1.9; text-align: justify; }

  .column-rule { position: absolute; left: 184px; top: 190px; bottom: 52px; border-left: 1px solid var(--soft-rule); }

  .report { position: absolute; left: 196px; right: 22px; top: 190px; height: 520px; }
  .report__head { font-size: 20px; font-weight: 900; margin-bottom: 10px; }
  .report__lead { position: absolute; left: 0; top: 40px; width: 160px; font-size: 12.5px; line-height: 1.9; text-align: justify; }
  .report__photo { position: absolute; left: 172px; top: 20px; right: 0; height: 256px; background: linear-gradient(180deg, var(--photo-dark), var(--photo-light) 70%, var(--photo-dark)); }
  .report__cols { position: absolute; left: 172px; right: 0; top: 292px; column-count: 3; column-gap: 18px; font-size: 12.5px; line-height: 1.9; text-align: justify; }

  .events { position: absolute; left: 196px; right: 22px; top: 720px; bottom: 52px; }
  .events__head { font-size: 18px; font-weight: 900; border-top: 3px solid var(--rule); border-bottom: 1px solid var(--rule); padding: 6px 0; }
  .events__grid { display: grid; grid-template-columns: 1fr 1fr; grid-template-rows: repeat(3, 1fr); gap: 14px 18px; position: absolute; left: 0; right: 0; top: 52px; bottom: 0; }
  .event-slot { border: 1.5px solid var(--rule); }

  .footer { position: absolute; left: 22px; right: 22px; bottom: 18px; border-top: 1px solid var(--rule); padding-top: 6px; text-align: right; font-size: 12px; }
</style>
</head>
<body>
  <header class="masthead">
    <p class="masthead__tagline">タマロ邸ホーム小倉のふれあい情報誌</p>
    <h1 class="masthead__title">豊かなくらし</h1>
    <div class="brand">Tamaro</div>
  </header>

  <aside class="sidebar">
    <div class="issue">No.4</div>
    <div class="issue-date">2015 年●月●日</div>
    <section class="topic">
      <h2 class="topic__head">■Topics</h2>
      <p class="topic__body">こんにちは！広報担当の森野です。長かった夏も終わり、朝晩はすっかり涼しくなりましたね。今年も予想以上の暑さでしたが、皆さまお元気でお過ごしでしょうか。そろそろ紅葉の便りも届く季節です。週末は家族で近くの公園へ出かけ、秋の空気を楽しみました。</p>
    </section>
    <section class="topic">
      <h2 class="topic__head">■Topics</h2>
      <p class="topic__body">こんにちは！広報担当の森野です。長かった夏も終わり、朝晩はすっかり涼しくなりましたね。今年も予想以上の暑さでしたが、皆さまお元気でお過ごしでしょうか。そろそろ紅葉の便りも届く季節です。週末は家族で近くの公園へ出かけ、秋の空気を楽しみました。</p>
    </section>
  </aside>

  <div class="column-rule"></div>

  <section class="report">
    <h2 class="report__head">ご報告</h2>
    <p class="report__lead">コヴァンタ改装ショップ全国コンテスト表彰式で、2015年CSアンケート部門(顧客満足度部門)において全国約430店の中から、当社が全国1位に選ばれました。2008年、2009年、2011年に続き、4年ぶり5回目の受賞となります。これもひとえに皆さまのおかげです。心より御礼申し上げます。</p>
    <div class="report__photo" role="img" aria-label="表彰式の壇上で受賞者が並ぶ写真"></div>
    <div class="report__cols">
      <p>受賞にあたり、スタッフ一同あらためて気持ちを引き締めております。これからも、皆さまの住まいの相談役として、誠実な家づくりを続けてまいります。今後ともご愛顧のほど、よろしくお願いいたします。ショールームのスタッフは、ご満足いただける工事とサービスを提供できるよう、日々努力してまいります。お住まいのことでお困りの際は、いつでもお気軽にご相談ください。</p>
    </div>
  </section>

  <section class="events">
    <h2 class="events__head">ショールームイベント日程</h2>
    <div class="events__grid">
      <div class="event-slot"></div>
      <div class="event-slot"></div>
      <div class="event-slot"></div>
      <div class="event-slot"></div>
      <div class="event-slot"></div>
      <div class="event-slot"></div>
    </div>
  </section>

  <footer class="footer">豊かなくらし No.4</footer>
</body>
</html>
```